Email Preference Page Design

We are looking for a 2 page design for our users to edit their email preferences and submit friend referrals. You can find the fuctionality, content and text here:

https://brightcart.examplemail.net/app/linkClick/7281/5c9a1b3e8d04f2aa/20583941/7f3d9e2b1a6c4058

* the shipping and billing address might be different so you need to show the billing if the "same as shipping" box is not checked. It can auto-hide like the page above shows if that fits your design.

* when the "unsubscribe from all email lists" box is selected, all the other checkbox options will hide as in the example page. We need you to show us what the site will look like with and without that checkbox selected.

We want to match these two pages to the general feel of these website pages:

www.brightcart.com
and
free.brightcart.com

The page should be very clean and tight. Project is for design only but must be able to be implemented in html showing button and checkbox states. Technically this must be two pages for our system - one for all the user info and one for individual email referrals (see example above).

Target Market(s)

video professionals

Industry/Entity Type

Shipping

Requirements
Must have
• our logo (see numerous versions attached)
well designed header
well designed sections
clean editable text
tight layout
html friendly
easy to understand
2 pages
Nice to have
• custom checkboxes and radio buttons

```html
<!DOCTYPE html>
<html lang="en">
<head>
<meta charset="utf-8">
<title>brightcart – Subscriber Communication Preferences</title>
<link rel="stylesheet" href="https://fonts.googleapis.com/css2?family=Bebas+Neue&family=Lato:wght@400;700&display=swap">
<style>
  :root {
    --page-bg: #eeeeec;
    --panel-bg: #fdfcfc;
    --panel-edge: #d9d9d7;
    --header-dark: #363c40;
    --header-dark-2: #2b3034;
    --accent: #ee6b1f;
    --label: #2d2d2d;
    --field-border: #c7c7c7;
    --field-bg: #ffffff;
    --sand-light: #fbf1dc;
    --sand-deep: #f3d797;
    --optout-bg: #e9e6e2;
    --button-top: #ffd666;
    --button-bottom: #f9b13a;
    --button-text: #8a5619;
    --logo-text: #ffffff;
  }
  * { box-sizing: border-box; margin: 0; padding: 0; }
  html, body { width: 972px; height: 1200px; overflow: hidden; }
  body {
    background: var(--page-bg);
    font-family: "Lato", Arial, sans-serif;
    color: var(--label);
  }
  .canvas { position: relative; width: 972px; height: 1200px; }

  /* Header */
  .page-title {
    position: absolute; left: 503px; top: 86px;
    font-family: "Bebas Neue", "Oswald", sans-serif;
    font-size: 29px; letter-spacing: 0.3px; color: var(--accent);
  }
  .header-shape { position: absolute; left: 79px; top: 89px; }
  .brand {
    position: absolute; left: 99px; top: 112px;
    display: flex; align-items: center; gap: 14px;
  }
  .brand-dot { width: 40px; height: 40px; border-radius: 50%; background: var(--accent); }
  .brand-name {
    font-family: "Lato", Arial, sans-serif; font-weight: 400;
    font-size: 50px; line-height: 1; color: var(--logo-text); letter-spacing: 0.5px;
  }

  /* Main form sheet */
  .sheet {
    position: absolute; left: 79px; top: 187px; width: 820px; height: 729px;
    background: var(--panel-bg);
    border: 1px solid var(--panel-edge); border-top: none;
    overflow: hidden;
  }
  .sand-band {
    position: absolute; left: 0; bottom: 0; width: 820px; height: 125px;
    background: linear-gradient(to bottom, rgba(251,241,220,0) 0%, var(--sand-light) 25%, var(--sand-deep) 100%);
  }

  .section-title {
    position: absolute; left: 100px;
    display: flex; align-items: center; gap: 6px;
    font-size: 17px; font-weight: 400; color: var(--accent);
  }
  .section-title svg { display: block; }

  .field-column { position: absolute; display: flex; flex-direction: column; }
  .field {
    display: flex; align-items: flex-end; gap: 11px;
    height: 28px; margin-bottom: 12px;
  }
  .field label {
    font-size: 13px; text-align: right; line-height: 1;
    padding-bottom: 2px;
  }
  .field-column.left label { width: 88px; }
  .field-column.right label { width: 92px; }
  .field input {
    width: 219px; height: 29px;
    border: 1px solid var(--field-border); border-radius: 2px;
    background: var(--field-bg);
  }

  .same-address {
    position: absolute; left: 101px; top: 384px;
    display: flex; align-items: center; gap: 5px; font-size: 13px;
  }
  .checkbox {
    width: 12px; height: 12px; border: 1px solid #8d8d8d;
    background: linear-gradient(#fff, #e4e4e4); border-radius: 1px;
    display: flex; align-items: center; justify-content: center;
  }

  /* Footer panel */
  .footer-panel {
    position: absolute; left: 79px; top: 930px; width: 820px; height: 187px;
    border: 1px solid var(--panel-edge); background: var(--panel-bg);
    overflow: hidden;
  }
  .opt-out {
    position: absolute; left: 279px; top: 26px; width: 269px; height: 46px;
    background: var(--optout-bg); border-radius: 2px;
    display: flex; align-items: center; justify-content: center; gap: 8px;
    font-size: 13px;
  }
  .opt-out .checkbox { background: linear-gradient(#fff, #dfe6f0); border-color: #7e8ba0; }
  .action-bar {
    position: absolute; left: 0; top: 95px; width: 820px; height: 92px;
    background: linear-gradient(var(--header-dark) 0%, var(--header-dark-2) 100%);
    border-top: 1px solid #22272a;
  }
  .save-button {
    position: absolute; left: 307px; top: 22px; width: 221px; height: 50px;
    border: 1px solid #d99325; border-radius: 2px;
    background: linear-gradient(var(--button-top), var(--button-bottom));
    font-family: "Lato", Arial, sans-serif; font-size: 18px; color: var(--button-text);
    box-shadow: inset 0 1px 0 rgba(255,255,255,0.5);
  }
</style>
</head>
<body>
<div class="canvas">

  <svg class="header-shape" width="820" height="99" viewBox="0 0 820 99" aria-hidden="true">
    <defs>
      <linearGradient id="headerFill" x1="0" y1="0" x2="0" y2="1">
        <stop offset="0" stop-color="#40474b"/>
        <stop offset="0.8" stop-color="#363c40"/>
        <stop offset="1" stop-color="#4a5054"/>
      </linearGradient>
    </defs>
    <path d="M4 0 H398 Q404 0 407 8 L414 30 Q417 39 426 39 H820 V98 H0 V4 Q0 0 4 0 Z" fill="url(#headerFill)"/>
  </svg>
  <div class="page-title">Subscriber Communication Preferences</div>
  <div class="brand">
    <span class="brand-dot"></span>
    <span class="brand-name">brightcart</span>
  </div>

  <form class="sheet">
    <h2 class="section-title" style="top:26px;">
      <svg width="14" height="17" viewBox="0 0 14 17" aria-hidden="true">
        <path d="M7 0 C3 0 0 3 0 6.6 C0 11 7 17 7 17 C7 17 14 11 14 6.6 C14 3 11 0 7 0 Z" fill="#ee6b1f"/>
        <circle cx="7" cy="6.5" r="2.4" fill="#fff"/>
      </svg>
      Contact information
    </h2>

    <div class="field-column left" style="left:81px; top:82px;">
      <div class="field"><label>First name</label><input type="text"></div>
      <div class="field"><label>Email</label><input type="text"></div>
      <div class="field"><label>Address line 1</label><input type="text"></div>
      <div class="field"><label>Address line 3</label><input type="text"></div>
      <div class="field"><label>Country</label><input type="text"></div>
      <div class="field"><label>Postal code</label><input type="text"></div>
    </div>
    <div class="field-column right" style="left:407px; top:82px;">
      <div class="field"><label>Last name</label><input type="text"></div>
      <div class="field"><label>Phone</label><input type="text"></div>
      <div class="field"><label>Address line 2</label><input type="text"></div>
      <div class="field"><label>City</label><input type="text"></div>
      <div class="field"><label>State</label><input type="text"></div>
    </div>

    <h2 class="section-title" style="top:349px;">
      <svg width="21" height="14" viewBox="0 0 21 14" aria-hidden="true">
        <rect x="0" y="1" width="12" height="9" fill="#ee6b1f"/>
        <path d="M12 4 H17 L20 7.5 V10 H12 Z" fill="#ee6b1f"/>
        <circle cx="4" cy="11.5" r="2.3" fill="#ee6b1f" stroke="#fff" stroke-width="1"/>
        <circle cx="16" cy="11.5" r="2.3" fill="#ee6b1f" stroke="#fff" stroke-width="1"/>
      </svg>
      Shipping Address
    </h2>
    <div class="same-address">
      <span class="checkbox"></span>
      My Billing address is same as shipping address.
    </div>

    <div class="field-column left" style="left:81px; top:436px;">
      <div class="field"><label>Address line 1</label><input type="text"></div>
      <div class="field"><label>Address line 3</label><input type="text"></div>
      <div class="field"><label>Country</label><input type="text"></div>
      <div class="field"><label>Postal code</label><input type="text"></div>
    </div>
    <div class="field-column right" style="left:407px; top:439px;">
      <div class="field"><label>Address line 2</label><input type="text"></div>
      <div class="field"><label>City</label><input type="text"></div>
      <div class="field"><label>State</label><input type="text"></div>
    </div>

    <div class="sand-band" role="img" aria-label="Decorative band of soft sand-coloured waves"></div>
  </form>

  <div class="footer-panel">
    <div class="opt-out">
      <span class="checkbox">
        <svg width="9" height="9" viewBox="0 0 9 9" aria-hidden="true"><path d="M1 4.5 L3.5 7 L8 1.5" stroke="#2f3f66" stroke-width="1.6" fill="none"/></svg>
      </span>
      Unsubscribe me from all email lists
    </div>
    <div class="action-bar">
      <button class="save-button" type="button">Save My Preferences</button>
    </div>
  </div>

</div>
</body>
</html>
```